Ravelor Global Kft. is an online recruitment marketplace connecting the employers and recruiters together. We provide an e-bussiness solution for companies and give busines opportunity for recruiters.
We have a logo design already, which should be used on the business card.
Our colours are grey and magenta, which can be seen in the logo. Black is also welcome.
The style should be dynamic, young but professional. It should be clear, visible, elegant, not too crowded, simple but exciting.
We need the following data on the BC: name, title, address, phone,fax and mobile number, email address, website.
Target Market(s)
Our target market are companies, as this is a B2B business. We also target recruiters, recruitment professionals, headhunters.We would like to be impressive and different.
Industry/Entity Type
Business
Requirements
Must have
- We would like to promote our website, www.ravelorglb.hu.
- Please, put this on the back with a quite visible letter size.The style should be dynamic, young but professional. It should be clear, visible, elegant, not too crowded, simple but exciting.
Should not have
- We do not want to see people figures.

```html
<!DOCTYPE html>
<html lang="en">
<head>
<meta charset="utf-8">
<title>Ravelor Global Kft. – Business Card</title>
<link rel="stylesheet" href="https://fonts.googleapis.com/css2?family=Arimo:wght@400;700&display=swap">
<style>
  :root {
    --paper: #ffffff;
    --mauve: #826f80;
    --magenta: #b3186f;
    --slate: #8a7b87;
    --ink-light: #ffffff;
  }
  * { margin: 0; padding: 0; box-sizing: border-box; }
  html, body {
    width: 1200px;
    height: 647px;
    overflow: hidden;
    background: var(--paper);
  }
  .card {
    position: relative;
    width: 1200px;
    height: 647px;
    background: var(--paper);
    font-family: "Arimo", Arial, sans-serif;
    color: var(--ink-light);
  }
  .brand {
    position: absolute;
    left: 12px;
    top: 262px;
    display: flex;
    align-items: center;
    gap: 14px;
  }
  .brand-mark { display: block; }
  .brand-name {
    font-weight: 700;
    font-size: 38px;
    letter-spacing: 1px;
    color: var(--magenta);
  }
  .info-panel {
    position: absolute;
    left: 367px;
    top: 0;
    width: 833px;
    height: 647px;
    background: var(--mauve);
    text-align: center;
  }
  .accent-band {
    position: absolute;
    left: 0;
    top: 164px;
    width: 100%;
    height: 17px;
    background: var(--magenta);
  }
  .line {
    position: absolute;
    left: 0;
    width: 100%;
    line-height: 1;
    white-space: nowrap;
  }
  .person-name { top: 22px; font-size: 49px; }
  .person-title { top: 100px; font-size: 41px; }
  .address { font-size: 29px; }
  .address-1 { top: 226px; }
  .address-2 { top: 261px; }
  .contact { font-size: 35px; letter-spacing: 1px; }
  .phone { top: 350px; }
  .fax { top: 392px; }
  .mobile { top: 433px; }
  .web { font-size: 36px; }
  .email { top: 541px; }
  .website { top: 583px; }
</style>
</head>
<body>
  <main class="card">
    <div class="brand">
      <svg class="brand-mark" width="110" height="110" viewBox="0 0 110 110" aria-hidden="true">
        <rect x="0" y="0" width="110" height="110" fill="var(--slate)"/>
      </svg>
      <span class="brand-name">RAVELOR</span>
    </div>

    <section class="info-panel">
      <p class="line person-name">Example Name</p>
      <p class="line person-title">Example Title</p>
      <div class="accent-band"></div>

      <p class="line address address-1">Address Line1</p>
      <p class="line address address-2">Address Line2</p>

      <p class="line contact phone">Phone:&nbsp; xxx.xx.xxxx</p>
      <p class="line contact fax">Fax:&nbsp; xxx.xx.xxxx</p>
      <p class="line contact mobile">Mobile:&nbsp; xxx.xx.xxxx</p>

      <p class="line web email">example@example.com</p>
      <p class="line web website">www.example.com</p>
    </section>
  </main>
</body>
</html>
```